Yoga Studio Postcard Advertising Flyer

Need a postcard size flyer that will promote our business. The objective is to promote location and availability. Want it to be personal. The objective to connect the audience to the purpose of yoga and the focus on enabling functional well-being. Something that is a very big focus at this point in time in the world. I really want people to see the value in connecting with us via our website, classora app, linkhive or pixly. The colours are to be bright but not overwhelming and aligned to the logo colours. Its also important to have the location picture on the flyer - unless you think that it is way too much (try a with or without). I don't want this to be a specials brochure - it is an introduction to our brand and our business. No need to over do it with promotional lines apart from come and join us.
Updates

Delayed in organising this.

Target Market(s)

Local yogis and residence who are or want to be focused on well-being.

Requirements
Must have
• Pictures - would have the logo on one side.
Nice to have
• Modern and aligned to website design.

```html
<!DOCTYPE html>
<html lang="en">
<head>
<meta charset="utf-8">
<title>Amber Lily Yoga – Postcard</title>
<link rel="stylesheet" href="https://fonts.googleapis.com/css2?family=Montserrat:wght@300;400;600;700;800;900&display=swap">
<style>
  :root {
    --navy: #16295e;
    --navy-deep: #122352;
    --sky: #29a8e0;
    --white: #ffffff;
    --ink: #1a1a1a;
    --page: #e9ebef;
    --line: #2a2a2a;
  }
  * { box-sizing: border-box; margin: 0; padding: 0; }
  html, body { width: 1200px; height: 615px; overflow: hidden; }
  body {
    background: var(--page);
    font-family: "Montserrat", sans-serif;
    position: relative;
  }
  .postcard {
    position: absolute;
    top: 117px;
    width: 540px;
    height: 380px;
    overflow: hidden;
    box-shadow: 0 6px 18px rgba(20, 30, 60, 0.18);
  }
  .postcard--back { left: 40px; background: var(--white); }
  .postcard--front { left: 620px; background: var(--navy); color: var(--white); }

  /* Back side */
  .back-panel { position: absolute; inset: 0; }
  .back-info {
    position: absolute;
    left: 24px; top: 22px;
    width: 215px;
    color: var(--white);
  }
  .wordmark {
    font-weight: 600;
    letter-spacing: 0.06em;
    text-transform: uppercase;
    display: flex;
    align-items: center;
    gap: 7px;
  }
  .wordmark__dot {
    width: 12px; height: 12px;
    border-radius: 50%;
    background: var(--sky);
    flex: none;
  }
  .wordmark--light { color: var(--white); font-size: 15px; }
  .wordmark--dark { color: var(--navy); font-size: 16px; }

  .values { list-style: none; margin-top: 16px; }
  .values__item {
    display: flex;
    align-items: center;
    gap: 9px;
    margin-bottom: 9px;
    font-size: 8.2px;
    line-height: 1.35;
    letter-spacing: 0.02em;
  }
  .values__icon {
    width: 24px; height: 24px;
    flex: none;
    border-radius: 50%;
    border: 1px solid var(--white);
    display: flex; align-items: center; justify-content: center;
  }
  .values__item:first-child .values__icon { background: var(--white); }

  .cta {
    font-weight: 900;
    text-transform: uppercase;
    letter-spacing: 0.01em;
  }
  .cta--back { color: var(--sky); font-size: 23px; margin-top: 4px; }
  .find-label {
    font-size: 8px; font-weight: 700;
    text-transform: uppercase;
    letter-spacing: 0.06em;
    margin-top: 9px;
  }
  .channels { display: flex; gap: 20px; margin-top: 8px; }
  .channel {
    display: flex; flex-direction: column; align-items: center; gap: 4px;
    font-size: 7px;
  }
  .channel__mark {
    width: 16px; height: 16px;
    border-radius: 50%;
    border: 2px solid var(--white);
  }
  .address { font-size: 8.5px; margin-top: 12px; line-height: 1.4; }
  .address strong { font-weight: 800; text-transform: uppercase; }

  .photo {
    position: absolute;
    width: 96px; height: 96px;
    border-radius: 50%;
    border: 3px solid var(--white);
  }
  .photo--venue { left: 252px; top: 22px; background: linear-gradient(160deg, #a9c3df 0%, #8b6d5a 55%, #5a4a40 100%); }
  .photo--teacher { left: 236px; top: 140px; background: linear-gradient(150deg, #e6e6e6 0%, #9a9a9a 60%, #4d4d4d 100%); }
  .photo--studio { left: 222px; top: 258px; background: linear-gradient(140deg, #e9e4de 0%, #b77b3f 50%, #2f3f66 100%); }

  .address-lines { position: absolute; left: 372px; top: 150px; width: 140px; }
  .address-lines span {
    display: block;
    border-bottom: 1.3px solid var(--line);
    height: 34px;
  }
  .stamp-box {
    position: absolute;
    right: 22px; top: 24px;
    width: 62px; height: 72px;
    border: 1.3px solid var(--line);
  }
  .back-logo { position: absolute; right: 24px; bottom: 24px; }

  /* Front side */
  .front-content { position: absolute; left: 34px; top: 30px; width: 300px; }
  .headline { margin-top: 24px; text-transform: uppercase; line-height: 1.02; }
  .headline__light { display: block; font-weight: 300; font-size: 32px; letter-spacing: 0.04em; }
  .headline__bold { display: block; font-weight: 800; font-size: 32px; }
  .vision {
    font-size: 10.5px;
    line-height: 1.35;
    letter-spacing: 0.03em;
    margin-top: 12px;
    width: 240px;
  }
  .site { font-weight: 700; font-size: 12px; margin-top: 10px; letter-spacing: 0.01em; }
  .cta--front { color: var(--white); font-size: 31px; margin-top: 22px; }
</style>
</head>
<body>

<section class="postcard postcard--back" aria-label="Postcard back">
  <svg class="back-panel" width="540" height="380" viewBox="0 0 540 380" aria-hidden="true">
    <path d="M0 0 H330 C 270 110, 235 250, 265 380 H0 Z" fill="var(--navy)"/>
  </svg>

  <div class="back-info">
    <div class="wordmark wordmark--light"><span class="wordmark__dot"></span>Amber Lily Yoga</div>

    <ul class="values">
      <li class="values__item">
        <span class="values__icon">
          <svg width="12" height="12" viewBox="0 0 12 12" aria-hidden="true"><circle cx="6" cy="3" r="1.6" fill="var(--navy)"/><path d="M2 10 L6 5 L10 10 Z" fill="var(--navy)"/></svg>
        </span>
        <span>Strengthen your well-being through adaptive yoga.</span>
      </li>
      <li class="values__item">
        <span class="values__icon">
          <svg width="12" height="12" viewBox="0 0 12 12" aria-hidden="true"><path d="M6 10 C 2 7, 1 4, 3.5 3 C 5 2.5, 6 4, 6 4 C 6 4, 7 2.5, 8.5 3 C 11 4, 10 7, 6 10 Z" fill="none" stroke="var(--white)" stroke-width="1"/></svg>
        </span>
        <span>Perfection is a desire and never an outcome through the practice of yoga</span>
      </li>
      <li class="values__item">
        <span class="values__icon">
          <svg width="12" height="12" viewBox="0 0 12 12" aria-hidden="true"><circle cx="6" cy="6" r="3.5" fill="none" stroke="var(--white)" stroke-width="1"/><circle cx="6" cy="6" r="1" fill="var(--white)"/></svg>
        </span>
        <span>Seek to evoke your mind and body through the challenge of yoga.</span>
      </li>
    </ul>

    <p class="cta cta--back">Come join us!</p>
    <p class="find-label">Find us on</p>
    <div class="channels">
      <div class="channel"><span class="channel__mark"></span><span>Classora App</span></div>
      <div class="channel"><span class="channel__mark"></span><span>Linkhive</span></div>
      <div class="channel"><span class="channel__mark"></span><span>Pixly</span></div>
    </div>
    <p class="address"><strong>The Chapel,</strong><br>842 Harbour Road Millbank NSW 2041</p>
  </div>

  <div class="photo photo--venue" role="img" aria-label="Photo of the studio venue, a brick chapel building"></div>
  <div class="photo photo--teacher" role="img" aria-label="Portrait photo of the yoga teacher"></div>
  <div class="photo photo--studio" role="img" aria-label="Photo of the studio interior with yoga mats laid out"></div>

  <div class="stamp-box" aria-hidden="true"></div>
  <div class="address-lines" aria-hidden="true"><span></span><span></span><span></span><span></span></div>

  <div class="back-logo wordmark wordmark--dark"><span class="wordmark__dot"></span>Amber Lily Yoga</div>
</section>

<section class="postcard postcard--front" aria-label="Postcard front">
  <div class="front-content">
    <div class="wordmark wordmark--light"><span class="wordmark__dot"></span>Amber Lily Yoga</div>
    <h1 class="headline">
      <span class="headline__light">Enable</span>
      <span class="headline__bold">Functional</span>
      <span class="headline__bold">Wellbeing</span>
    </h1>
    <p class="vision">Our vision is to create an atmosphere that enables inclusiveness of the whole community</p>
    <p class="site">www.amberlilyyoga.com.au</p>
    <p class="cta cta--front">Come join us!</p>
  </div>
</section>

</body>
</html>
```